Kovix Tralo Mart Listing Screenshot Design

We would like to create new screenshots for our Kovix app in the Tralo Mart to A/B test against the current version.

You can view our current Kovix Tralo Mart listing here: https://apps.tralomart.example/listing?id=com.quorvantic.kovix&hl=en

Attached I have added screenshots of the app that I would like to be included. Please edit the screenshots to generic text (e.g. John Smith, 123 Main St, etc.).

You can use the same text we have in the current ones. For text for the criminal screenshot please view our Zyn Zeph Shop listing: https://apps.zephshop.example/us/app/quorvantic-background-check/id907164352?mt=8

If you want to come up with new text please feel free to!

I also attached a few examples of other app screenshots that we like.

Kovix TraloMart Listing Guidelines: https://help.tralomart.example/tralomart/kovix-developer/answer/5526193?hl=en

Industry/Entity Type

Store

Font styles to use
Sans Serif

Colors
f0f0f0

Requirements
Must have
• ~Generic names and data like "John Smith", "54 Main St. Springfield, NJ 09876"
• ~Screenshot for Person Search, Criminal Records, Phone Search, Email Search, and Property Search. In that order.
• ~Headlines either the ones used in our current screenshots (https://apps.tralomart.example/listing?id=com.quorvantic.kovix&hl=en) or new ones you come up with.
• ~Must meet Kovix screenshot guidelines.
• ~Optimized for downloads.
• Must use following color palette:
• Dark purple #3B2469
• Light purple #7E6F9C
• Very dark gray #333333
• Dark gray #666666
• Gray #999999
• Blue gray #CFD9DE
• Green #5CB85C
• Navy #003577
• Yellow #F3B607
• Magenta #F0386B

```html
<!DOCTYPE html>
<html lang="en">
<head>
<meta charset="utf-8">
<title>Kovix – Email Search</title>
<link rel="stylesheet" href="https://fonts.googleapis.com/css2?family=Montserrat:wght@500;600&family=Roboto:wght@400;500;700&display=swap">
<style>
  :root {
    --bg-top: #231a63;
    --bg-bottom: #1f5aa8;
    --dark-purple: #2c1a5c;
    --app-bar: #2f1c60;
    --header-purple: #645b8e;
    --heading: #2d1a5e;
    --very-dark-gray: #333333;
    --text: #1d1d1d;
    --muted: #8a8f99;
    --band: #e3e5ea;
    --box-border: #cfd2d6;
    --icon-gray: #c9cbcf;
    --green: #5cb85c;
    --white: #ffffff;
  }
  * { box-sizing: border-box; margin: 0; padding: 0; }
  html, body { width: 675px; height: 1200px; overflow: hidden; }
  body {
    position: relative;
    background: linear-gradient(180deg, var(--bg-top) 0%, var(--bg-top) 20%, var(--bg-bottom) 100%);
    font-family: "Roboto", Arial, sans-serif;
  }
  .headline {
    position: absolute; top: 66px; left: 0; width: 675px;
    text-align: center; color: var(--white);
    font-family: "Montserrat", Arial, sans-serif; font-weight: 600;
    font-size: 41px; line-height: 54px; letter-spacing: 0.3px;
  }
  .screen {
    position: absolute; left: 108px; top: 348px; width: 460px; height: 816px;
    background: var(--white); overflow: hidden;
  }
  .status-bar {
    position: absolute; top: 0; left: 0; width: 100%; height: 30px;
    background: var(--dark-purple); color: #e6e4ee;
  }
  .status-bar .time { position: absolute; right: 12px; top: 4px; font-size: 19px; }
  .status-bar .battery-pct { position: absolute; right: 120px; top: 8px; font-size: 13px; }
  .app-bar {
    position: absolute; top: 30px; left: 0; width: 100%; height: 72px;
    background: var(--app-bar); color: var(--white);
  }
  .app-bar .title { position: absolute; left: 91px; top: 23px; font-size: 22px; font-weight: 500; }
  .report-header {
    position: absolute; top: 102px; left: 0; width: 100%; height: 190px;
  }
  .report-email {
    position: absolute; top: 124px; left: 0; width: 100%; text-align: center;
    color: #f1eff7; font-size: 21px; text-decoration: underline; text-underline-offset: 3px;
  }
  .avatar {
    position: absolute; left: 152px; top: 166px; width: 156px; height: 156px; border-radius: 50%;
    background: radial-gradient(circle at 50% 40%, #9a9a9a 0%, #5e5e5e 60%, #2e2e2e 100%);
    box-shadow: 0 4px 10px rgba(0,0,0,0.35);
  }
  .section-title {
    position: absolute; left: 7px; color: var(--heading); font-size: 32px; font-weight: 400;
  }
  .overview-title { top: 340px; }
  .owner-label {
    position: absolute; left: 7px; top: 396px; color: var(--muted); font-size: 17px; font-weight: 500;
  }
  .owner-name { position: absolute; left: 7px; top: 428px; color: var(--text); font-size: 19px; }
  .aliases-band {
    position: absolute; left: 0; top: 468px; width: 100%; height: 42px; background: var(--band);
    text-align: center; line-height: 42px; color: #5a5d63; font-size: 18px;
  }
  .empty-box {
    position: absolute; left: 10px; top: 526px; width: 440px; height: 220px;
    border: 2px solid var(--box-border); text-align: center;
  }
  .empty-box svg { margin-top: 27px; }
  .empty-title { margin-top: 28px; font-size: 17px; font-weight: 700; color: var(--text); }
  .empty-text { margin-top: 4px; font-size: 16px; line-height: 21px; color: var(--text); padding: 0 20px; }
  .social-title { top: 786px; }
  .help-circle { position: absolute; left: 419px; top: 786px; }
  .fab {
    position: absolute; left: 368px; top: 724px; width: 72px; height: 72px; border-radius: 50%;
    background: var(--green); box-shadow: 0 3px 8px rgba(0,0,0,0.3);
    display: flex; align-items: center; justify-content: center;
  }
</style>
</head>
<body>
  <h1 class="headline">Check out hidden social<br>media profiles</h1>

  <main class="screen">
    <div class="status-bar">
      <svg width="120" height="30" viewBox="0 0 120 30" style="position:absolute;left:14px;top:0">
        <rect x="2" y="7" width="16" height="16" fill="none" stroke="#d8d6e2" stroke-width="2"/>
        <path d="M5 20 L9 14 L12 18 L14 16 L16 20 Z" fill="#d8d6e2"/>
        <rect x="30" y="9" width="16" height="13" fill="#d8d6e2"/>
        <rect x="64" y="7" width="13" height="17" fill="#ececec"/>
        <path d="M67 13 L74 20 M74 13 L67 20" stroke="#c0392b" stroke-width="2"/>
      </svg>
      <svg width="110" height="30" viewBox="0 0 110 30" style="position:absolute;left:218px;top:0">
        <path d="M4 12 H9 L15 7 V23 L9 18 H4 Z" fill="#d8d6e2"/>
        <path d="M2 6 L22 24" stroke="#d8d6e2" stroke-width="2"/>
        <path d="M34 11 Q44 3 54 11 M37 15 Q44 9 51 15 M40 19 Q44 15 48 19" stroke="#d8d6e2" stroke-width="2" fill="none"/>
        <circle cx="44" cy="23" r="2" fill="#d8d6e2"/>
        <path d="M66 24 L84 6 V24 Z" fill="#9d98b4"/>
      </svg>
      <span class="battery-pct">18%</span>
      <svg width="14" height="22" viewBox="0 0 14 22" style="position:absolute;right:104px;top:5px">
        <rect x="1" y="3" width="12" height="18" fill="none" stroke="#d8d6e2" stroke-width="1.5"/>
        <rect x="4" y="0" width="6" height="3" fill="#d8d6e2"/>
        <rect x="2" y="15" width="10" height="5" fill="#d8d6e2"/>
      </svg>
      <span class="time">5:11 PM</span>
    </div>

    <header class="app-bar">
      <svg width="26" height="26" viewBox="0 0 26 26" style="position:absolute;left:29px;top:23px">
        <path d="M24 13 H3 M12 4 L3 13 L12 22" stroke="#fff" stroke-width="2.5" fill="none" stroke-linecap="round" stroke-linejoin="round"/>
      </svg>
      <span class="title">Email Report</span>
      <svg width="32" height="34" viewBox="0 0 32 34" style="position:absolute;left:353px;top:18px">
        <path d="M16 3 C9 3 7 9 7 14 V21 L3 26 H29 L25 21 V14 C25 9 23 3 16 3 Z" fill="none" stroke="#fff" stroke-width="2.2" stroke-linejoin="round"/>
        <path d="M12 29 Q16 33 20 29" stroke="#fff" stroke-width="2.2" fill="none"/>
        <path d="M16 10 V20 M11 15 H21" stroke="#fff" stroke-width="2.2"/>
      </svg>
      <svg width="30" height="30" viewBox="0 0 30 30" style="position:absolute;left:413px;top:21px">
        <circle cx="15" cy="15" r="13" fill="none" stroke="#fff" stroke-width="2.2"/>
        <path d="M11 12 Q11 7.5 15 7.5 Q19 7.5 19 11.5 Q19 14 15.5 15.5 V18" stroke="#fff" stroke-width="2.2" fill="none"/>
        <circle cx="15.5" cy="22" r="1.5" fill="#fff"/>
      </svg>
    </header>

    <svg class="report-header" viewBox="0 0 460 190" preserveAspectRatio="none">
      <polygon points="0,0 460,0 460,152 0,190" fill="var(--header-purple)"/>
    </svg>
    <div class="report-email">marlo@quillpost.example</div>
    <div class="avatar" role="img" aria-label="Black and white portrait photo of the email owner"></div>

    <h2 class="section-title overview-title">Email Overview</h2>
    <div class="owner-label">OWNER</div>
    <div class="owner-name">Marlo Dentrik</div>

    <div class="aliases-band">ALIASES</div>
    <div class="empty-box">
      <svg width="52" height="52" viewBox="0 0 52 52">
        <path d="M3 3 H49 V39 H13 L3 50 Z" fill="var(--icon-gray)"/>
        <rect x="24" y="11" width="4" height="13" fill="#fff"/>
        <rect x="24" y="28" width="4" height="4" fill="#fff"/>
      </svg>
      <div class="empty-title">No Aliases Were Found</div>
      <div class="empty-text">We searched for aliases, unfortunately there was no data.</div>
    </div>

    <h2 class="section-title social-title">Social Media &amp; Websites</h2>
    <svg class="help-circle" width="32" height="32" viewBox="0 0 32 32">
      <circle cx="16" cy="16" r="14" fill="none" stroke="#a7aab0" stroke-width="2.2"/>
      <path d="M12 13 Q12 8.5 16 8.5 Q20 8.5 20 12.5 Q20 15 16.5 16.5 V19" stroke="#a7aab0" stroke-width="2.2" fill="none"/>
      <circle cx="16.5" cy="23" r="1.5" fill="#a7aab0"/>
    </svg>

    <div class="fab">
      <svg width="26" height="20" viewBox="0 0 26 20">
        <rect x="0" y="2" width="3" height="3" fill="#fff"/><rect x="6" y="2" width="20" height="3" fill="#fff"/>
        <rect x="0" y="8.5" width="3" height="3" fill="#fff"/><rect x="6" y="8.5" width="20" height="3" fill="#fff"/>
        <rect x="0" y="15" width="3" height="3" fill="#fff"/><rect x="6" y="15" width="20" height="3" fill="#fff"/>
      </svg>
    </div>
  </main>
</body>
</html>
```